Visit card for Luxury Alpine home

Velvet Ridge Chalet (Hinterthal, Austria) – visit card

Brief: To design a visit card (4/4) that can be both left for existing guests and handed out to friends/business contacts to promote our luxury holiday home in the Austrian alps which can be rented year -round but primarily for summer (hiking/biking/golf) and winter (skiing). Primary focus is for family as its a 3br/3ba place that is usually booked for either a larger family or two families.

Basic information required/purpose: email/contact info. Basic information about the place, location, possibly some ideas/icons about what to do. Imagery that gives people the idea about luxury/fun/mountains etc. Hopefully the card would be something to interest them enough to check out the website and eventually make a direct booking with us.

Our details and photos:

https://velvetridgechalet.com
https://www.facebook.com/velvetridgechalet/

contact information for people to book:
stay.brenvale@larkpost.net
+420 604918352

some other resources:

http://www.tamrisberg-info.at/en/vacation.html
the moutains are called Hochkoenig and our village is Hinterthal which is next to Maria alm

Target Market(s)

European (winter) and Middle-Eastern (summer) families.

Industry/Entity Type

Travel

Contact Information for Business Card

standard 4/4 to be used for prospect

Font styles to use
Sans Serif

Colors

Designer to choose colors to be used in the design.

Requirements
Must have
• all relevant information for the client to contact us
• colorful/luxury imagery of the property (we can provide better photo quality that the web downloads)
Nice to have
• not particular about fonts. preferring subdued colours

```html
<!DOCTYPE html>
<html lang="en">
<head>
<meta charset="utf-8">
<title>Velvet Ridge Chalet – Visit Card</title>
<link href="https://fonts.googleapis.com/css2?family=Oswald:wght@300;400&family=Fira+Sans+Condensed:wght@400;600;700&display=swap" rel="stylesheet">
<style>
  :root{
    --bg:#1d1d1f;
    --gold-light:#fbdc84;
    --gold:#f3c65a;
    --gold-line:#e2b54a;
    --ink:#2a2217;
    --navy:#23253a;
    --wood-light:#d9b27a;
    --wood:#a97a45;
    --wood-dark:#5a3d22;
    --cream:#efe3c8;
  }
  *{box-sizing:border-box;margin:0;padding:0}
  html,body{width:1200px;height:890px;overflow:hidden;background:var(--bg)}
  .canvas{position:relative;width:1200px;height:890px}
  .card{position:absolute;left:260px;width:680px;height:390px;overflow:hidden;box-shadow:0 12px 30px rgba(0,0,0,.5)}
  .card-front{top:35px;background:linear-gradient(135deg,var(--gold-light),var(--gold))}
  .card-back{top:465px;background:var(--cream)}
  .card svg{position:absolute;inset:0}
  .brand-block{position:absolute;left:26px;bottom:34px;color:var(--gold);font-family:'Oswald',sans-serif}
  .brand-name{font-weight:300;font-size:40px;letter-spacing:1px;line-height:1;text-transform:uppercase}
  .brand-tagline{font-weight:300;font-size:13px;letter-spacing:3px;text-transform:uppercase;margin-top:6px;color:#f6d98c}
  .info{position:absolute;left:380px;top:28px;width:280px;font-family:'Fira Sans Condensed',sans-serif;color:var(--ink)}
  .intro{text-align:center;font-size:14px;line-height:1.35}
  .booking-note{text-align:center;font-size:14px;margin-top:14px}
  .platforms{display:flex;justify-content:center;gap:20px;margin-top:8px;font-weight:700;font-size:22px}
  .contact-head{font-weight:700;font-size:16px;margin-top:16px;padding-left:78px}
  .contact-list{list-style:none;margin-top:4px;padding-left:48px;font-size:13.5px;line-height:1.55}
  .contact-list b{display:inline-block;width:22px;font-weight:600}
  .social-dot{display:inline-block;width:11px;height:11px;border:1px solid var(--ink);border-radius:50%;margin-right:8px;vertical-align:-1px}
</style>
</head>
<body>
<div class="canvas">

  <section class="card card-front">
    <svg width="680" height="390" viewBox="0 0 680 390">
      <defs>
        <linearGradient id="bedroomTone" x1="0" y1="0" x2="1" y2="1">
          <stop offset="0" stop-color="#c99a5c"/>
          <stop offset=".5" stop-color="#8e6a45"/>
          <stop offset="1" stop-color="#3e3040"/>
        </linearGradient>
      </defs>
      <polygon points="0,0 190,0 430,390 0,390" fill="var(--navy)"/>
      <polygon role="img" aria-label="Photo of the chalet bedroom with timber ceiling and mountain window" points="0,0 175,0 412,390 0,390" fill="url(#bedroomTone)"/>
    </svg>
    <div class="brand-block">
      <div class="brand-name">Velvet Ridge Chalet</div>
      <div class="brand-tagline">Luxury rental apartment in Hinterthal</div>
    </div>
    <div class="info">
      <p class="intro">Experience genuine exhilaration with Velvet Ridge Chalet<br>and celebrate the luxury life in Hinterthal.</p>
      <p class="booking-note">Our apartment can be booked through</p>
      <div class="platforms"><span>Roomfinder</span><span>Homeshare</span></div>
      <p class="contact-head">or contact us via</p>
      <ul class="contact-list">
        <li><b>T:</b>+420 604 918 352</li>
        <li><b>E:</b>stay.brenvale@larkpost.net</li>
        <li><b>W:</b>www.velvetridgechalet.com</li>
        <li><b></b><span class="social-dot"></span>@velvetridgechalet</li>
      </ul>
    </div>
  </section>

  <section class="card card-back">
    <svg width="680" height="390" viewBox="0 0 680 390">
      <defs>
        <linearGradient id="livingTone" x1="0" y1="0" x2="1" y2="1">
          <stop offset="0" stop-color="#e6c48c"/>
          <stop offset="1" stop-color="#9c7446"/>
        </linearGradient>
        <linearGradient id="diningTone" x1="0" y1="0" x2="1" y2="1">
          <stop offset="0" stop-color="#d8b27c"/>
          <stop offset=".6" stop-color="#8a5f36"/>
          <stop offset="1" stop-color="#4c3420"/>
        </linearGradient>
        <linearGradient id="bedTone" x1="0" y1="0" x2="1" y2="0">
          <stop offset="0" stop-color="#3d3540"/>
          <stop offset="1" stop-color="#c29561"/>
        </linearGradient>
      </defs>
      <polygon role="img" aria-label="Photo of the living room with antler chandelier and mountain painting" points="0,0 330,0 380,250 0,330" fill="url(#livingTone)"/>
      <polygon role="img" aria-label="Photo of the dining table beside the fireplace" points="330,0 680,0 680,390 430,390 470,300 380,250" fill="url(#diningTone)"/>
      <polygon role="img" aria-label="Photo of the bedroom with timber beams" points="0,330 380,250 470,300 430,390 0,390" fill="url(#bedTone)"/>
      <polyline points="330,0 380,250 0,330" fill="none" stroke="var(--gold-line)" stroke-width="2"/>
      <polyline points="380,250 470,300 430,390" fill="none" stroke="var(--gold-line)" stroke-width="2"/>
      <polyline points="250,0 380,250" fill="none" stroke="var(--gold-line)" stroke-width="1"/>
    </svg>
  </section>

</div>
</body>
</html>
```